Modernize and improve usability of our webpage www.lernwandel.ch (4 languages, mostly static content)

Need to modernize and freshen up the webpages of our association: www.lernwandel.ch We offer apprenticeship exchanges within Switzerland and abroad. Young people can inform and enroll online. We do the matchmaking with work locations and organize logistics, stay overs etc.
The webpage needs to be in 4 languages (German, French, Italian and English). The main pages will be:
- Landing page: what we do, targeted to our apprentices / young people who enroll for the stages.
- Sup-Page: Registration form for interested apprentices to sign up for the program
- Sub-Page "Company", the firms who would like to send their apprentices on a internship and info on how to join the program
- Sub-Page "Host Family", private people who would be interested in hosting the apprentices (for free) during the stages. Find out about the reqiurements for the host families
- Sub-Page "About Us", who we are, executive team, board of director, our sponsor "Corvina Circle Switzerland"
- Footer: contact (E-Mail, Telephone, plain social circle), Bank details (IBAN Number), Partnerlogo of Corvina-Circle (see uploaded jpg), Social-Media Links (plain social circle, plain social circle)

Target Market(s)

Young people looking for a "apprenticeship" stage within Switzerland or going from Switzerland abroad

Industry/Entity Type

Apprenticeships: cooks, builders, craftsman, office support, etc.

Font styles to use
Other font styles liked:
• Lato (sans serif)

Requirements
Must have
• use colors shown on uploaded PDF-Slides: Make the BLUE the MAIN color, the ORANGE as a secondary color
Nice to have
• Forms using e.g. google forms or survey-monkey forms (external links, no code). Matching & appealing visuals showing young apprentices (can use stock photos)

```html
<!DOCTYPE html>
<html lang="en">
<head>
<meta charset="utf-8">
<title>lernwandel – Apprentice Exchange</title>
<link href="https://fonts.googleapis.com/css2?family=Lato:wght@400;700&family=Nunito:wght@700;800;900&display=swap" rel="stylesheet">
<style>
:root{
  --blue:#234f86;
  --blue-dark:#1b3f6e;
  --orange:#c84d0f;
  --sky:#3fb0f0;
  --ink:#1b1b1b;
  --text:#333;
  --footer:#0e0f14;
  --white:#fff;
}
*{box-sizing:border-box;margin:0;padding:0}
html,body{width:1200px;height:3938px;overflow:hidden}
body{font-family:'Lato',sans-serif;color:var(--text);background:var(--white);position:relative}
section,header,footer{position:relative;width:1200px;overflow:hidden}
.abs{position:absolute}
a{color:inherit;text-decoration:none}

/* header */
.site-header{height:102px;background:var(--white)}
.topbar{left:329px;top:0;width:871px;height:47px;background:var(--blue);clip-path:polygon(0 0,100% 0,100% 100%,46px 100%);color:var(--white);font-size:15px}
.topbar .item{position:absolute;top:0;height:47px;display:flex;align-items:center;gap:14px}
.dot-icon{width:32px;height:32px;border-radius:50%;background:var(--white);display:flex;align-items:center;justify-content:center}
.social{position:absolute;top:7px;width:32px;height:32px;border-radius:50%;background:var(--white)}
.brand{left:100px;top:26px;font-family:'Nunito',sans-serif;font-weight:800;font-size:40px;color:var(--orange);letter-spacing:-0.5px;line-height:1}
.nav{left:419px;top:66px;display:flex;gap:0;font-size:15px;color:var(--ink)}
.nav a{position:absolute;white-space:nowrap}

/* hero */
.hero{height:585px;background:linear-gradient(100deg,#5d6670 0%,#2e3338 30%,#3a4a52 55%,#1d2a33 100%)}
.hero-photo{inset:0}
.hero h1{left:696px;top:116px;font-family:'Nunito',sans-serif;font-weight:900;font-size:66px;line-height:80px;color:var(--white)}
.hero p{left:696px;top:282px;width:430px;font-size:14px;line-height:29px;color:var(--white)}
.btn{display:flex;align-items:center;justify-content:center;border-radius:24px;font-weight:700;font-size:14px}
.hero .btn{left:696px;top:393px;width:131px;height:43px;background:var(--blue);color:var(--white)}
.slide-arrow{top:265px;width:28px;height:28px;border:1.5px solid var(--white);border-radius:50%}

/* about */
.about{height:597px}
.about h2{left:99px;top:86px;font-family:'Nunito',sans-serif;font-weight:900;font-size:44px;color:var(--ink)}
.about p{left:99px;top:150px;width:465px;font-size:14px;line-height:28.7px;color:var(--ink)}
.about .btn{left:99px;top:431px;width:131px;height:46px;background:var(--blue);color:var(--white)}
.about-photo{left:657px;top:75px;width:420px;height:420px;border-radius:50%;border:4px solid var(--blue);padding:10px;background:var(--white)}
.about-photo div{width:100%;height:100%;border-radius:50%;background:linear-gradient(160deg,#8e9aa2,#566470 55%,#2b3f66)}

/* benefits band */
.benefits{height:487px;background:linear-gradient(180deg,#2a5892,#224c82)}
.card{top:115px;width:474px;height:288px;background:var(--white);border-radius:5px;text-align:center}
.card-icon{top:-48px;left:176px;width:122px;height:122px;border-radius:50%;background:var(--white);display:flex;align-items:center;justify-content:center}
.card-icon span{width:106px;height:106px;border-radius:50%;display:flex;align-items:center;justify-content:center}
.card h3{position:absolute;top:96px;left:0;right:0;font-size:17px;font-weight:400;color:var(--ink)}
.card p{position:absolute;top:127px;left:20px;right:20px;font-size:14px;line-height:29px;color:var(--ink)}
.card a{position:absolute;top:218px;left:0;right:0;font-size:14px;text-decoration:underline;font-weight:700;color:var(--ink)}

/* what we do */
.what{height:824px}
.section-title{left:0;right:0;text-align:center;font-family:'Nunito',sans-serif;font-weight:800;font-size:44px;color:var(--ink)}
.what .lead{left:150px;top:145px;width:900px;text-align:center;font-size:14px;line-height:31px;color:var(--ink)}
.step-icon{width:88px;height:88px;border-radius:50%;display:flex;align-items:center;justify-content:center}
.step-text{font-size:14px;line-height:30px;color:var(--ink);white-space:nowrap}
.step-text.left{text-align:right}
.hub-name{left:399px;top:346px;width:400px;text-align:center;font-family:'Nunito',sans-serif;font-weight:800;font-size:48px;color:var(--blue);line-height:1}

/* contact */
.contact{height:532px;background:linear-gradient(180deg,#2a5892,#234f86)}
.contact .section-title{color:var(--white);top:62px}
.field{border:2px solid rgba(255,255,255,.9);border-radius:6px;color:var(--white);font-size:14px;padding:14px 16px}
.contact .btn{left:531px;top:390px;width:137px;height:49px;background:var(--white);color:var(--blue);border-radius:25px;font-size:16px}

/* partners */
.partners{height:402px}
.partner{top:165px;width:179px;height:138px;border-radius:8px;background:var(--white);box-shadow:0 3px 12px rgba(0,0,0,.12);display:flex;align-items:center;justify-content:center}
.partner span{width:110px;height:44px;border-radius:6px;background:#e3e6ea}

/* footer */
.site-footer{height:409px;background:var(--footer);color:var(--white)}
.footer-brand{left:99px;top:70px;font-family:'Nunito',sans-serif;font-weight:800;font-size:42px;line-height:1}
.f-social{top:149px;width:32px;height:32px;border-radius:50%;background:var(--white)}
.iban-label{left:99px;top:210px;font-size:20px;font-weight:700}
.iban{left:99px;top:246px;font-size:17px;color:#ddd}
.f-col h4{font-family:'Nunito',sans-serif;font-size:21px;font-weight:800;margin-bottom:10px}
.f-col ul{list-style:none}
.f-col li{font-size:15px;height:31px;display:flex;align-items:center;gap:14px}
.f-contact li{height:59px;gap:22px}
.f-pin{width:36px;height:36px;border-radius:50%;background:var(--white);display:flex;align-items:center;justify-content:center;flex:none}
.rule{left:99px;top:339px;width:1002px;height:1px;background:#8a8a8a}
.copyright{left:99px;top:362px;font-size:15px}
.sponsor{right:99px;top:356px;display:flex;align-items:center;gap:8px;font-size:20px;font-weight:700;color:var(--sky)}
.sponsor i{width:30px;height:30px;border-radius:50%;background:#d9a21b;display:block}
</style>
</head>
<body>
<svg width="0" height="0" style="position:absolute">
  <defs>
    <symbol id="coin-hand" viewBox="0 0 48 48">
      <g fill="none" stroke="#fff" stroke-width="2" stroke-linecap="round" stroke-linejoin="round">
        <circle cx="24" cy="19" r="9"/>
        <path d="M24 14v10M21.5 16.5c0-1.2 1.1-2 2.5-2s2.5.8 2.5 2-1.1 1.8-2.5 2.2-2.5 1-2.5 2.2 1.1 2 2.5 2 2.5-.8 2.5-2"/>
        <path d="M24 4v3M18 6l1.2 2.5M30 6l-1.2 2.5"/>
        <path d="M6 34h6v9H6zM12 36h8c2 0 3 1 3 2.5s-1 2.5-3 2.5h-4M23 39l10-4c2-.8 4 .5 3 2.5l-12 6H12"/>
      </g>
    </symbol>
    <symbol id="growth" viewBox="0 0 48 48">
      <g fill="none" stroke="#fff" stroke-width="2" stroke-linecap="round" stroke-linejoin="round">
        <circle cx="14" cy="14" r="7"/>
        <path d="M14 10v8M12 12c0-1 .9-1.5 2-1.5s2 .5 2 1.5-2 1.5-2 1.5-2 .5-2 1.5.9 1.5 2 1.5 2-.5 2-1.5"/>
        <path d="M8 42V34M16 42V30M24 42V26M32 42V22M40 42V18M4 42h40M24 18l14-10M33 8h5v5"/>
      </g>
    </symbol>
  </defs>
</svg>

<header class="site-header">
  <div class="abs topbar">
    <div class="item" style="left:114px"><span class="dot-icon"><svg width="14" height="14" viewBox="0 0 24 24"><path fill="#234f86" d="M6.6 10.8a15 15 0 0 0 6.6 6.6l2.2-2.2a1 1 0 0 1 1-.25 11 11 0 0 0 3.6.6 1 1 0 0 1 1 1V20a1 1 0 0 1-1 1A17 17 0 0 1 3 4a1 1 0 0 1 1-1h3.5a1 1 0 0 1 1 1 11 11 0 0 0 .6 3.6 1 1 0 0 1-.25 1z"/></svg></span>+41 (0) 31 555 01 23</div>
    <div class="item" style="left:357px"><span class="dot-icon"><svg width="14" height="12" viewBox="0 0 24 18"><path fill="#234f86" d="M0 2l12 8 12-8V0H0zM0 4.5V18h24V4.5l-12 8z"/></svg></span>info@lernwandel.ch</div>
    <div class="item" style="left:560px;gap:6px;font-family:serif;font-size:14px"><svg width="18" height="18" viewBox="0 0 24 24" fill="none" stroke="#fff" stroke-width="1.6"><circle cx="12" cy="12" r="10"/><path d="M2 12h20M12 2c3 3 3 17 0 20M12 2c-3 3-3 17 0 20"/></svg>▾ En</div>
    <span class="social" style="left:664px" aria-label="Social network link"></span>
    <span class="social" style="left:707px" aria-label="Social network link"></span>
    <span class="social" style="left:750px" aria-label="Social network link"></span>
  </div>
  <div class="abs brand">lernwandel</div>
  <nav class="abs nav">
    <a style="left:0">Home</a>
    <a style="left:76px">What we do</a>
    <a style="left:193px">Registration</a>
    <a style="left:313px">Company</a>
    <a style="left:412px">Host Family</a>
    <a style="left:529px">About Us</a>
    <a style="left:627px">Contact</a>
  </nav>
</header>

<section class="hero">
  <div class="abs hero-photo" role="img" aria-label="Young apprentice in a winter jacket and beanie beside a mountain lake"></div>
  <span class="abs slide-arrow" style="left:42px"><svg width="25" height="25" viewBox="0 0 25 25"><path d="M14 8l-5 4.5 5 4.5" fill="none" stroke="#fff" stroke-width="1.5"/></svg></span>
  <span class="abs slide-arrow" style="left:1129px"><svg width="25" height="25" viewBox="0 0 25 25"><path d="M11 8l5 4.5-5 4.5" fill="none" stroke="#fff" stroke-width="1.5"/></svg></span>
  <h1 class="abs">Welcome To<br>Lernwandel</h1>
  <p class="abs">Lernwandel has been organizing the exchange of apprentices between different cultural and language regions within Switzerland as well as with other countriesmore than 19 years.</p>
  <a class="abs btn">Get Started</a>
</section>

<section class="about">
  <h2 class="abs">About Us</h2>
  <p class="abs">Lernwandel has been organizing the exchange of apprentices between different cultural and language regions within Switzerland as well as with other countries for more than 19 years. Primary participants are all apprentices who are completing their basic vocational education and training. Once registered for the exchange, lernwandel will find a suitable exchange company and an appropriate accommodation, where the apprentice will go through an exchange of at least three weeks. Corvina Circle Switzerland/Liechtenstein mainly supports this program with the objective of promoting the mobility of apprentices.</p>
  <a class="abs btn">Read More</a>
  <div class="abs about-photo"><div role="img" aria-label="Smiling apprentice in a navy sweater leaning on shelving in a workshop"></div></div>
</section>

<section class="benefits">
  <div class="abs card" style="left:99px">
    <div class="abs card-icon"><span style="background:var(--orange)"><svg width="52" height="52"><use href="#growth"/></svg></span></div>
    <h3>PROFIT</h3>
    <p>By taking part in this exchange programme, you broaden your professional as well as your personal horizon. Not only do you get to know a new environment, and flexibility.</p>
    <a>Read More</a>
  </div>
  <div class="abs card" style="left:627px">
    <div class="abs card-icon"><span style="background:var(--sky)"><svg width="52" height="52"><use href="#coin-hand"/></svg></span></div>
    <h3>COSTS</h3>
    <p>Your training company continues paying your normal wage during the exchange. Whenever possible you live with a host family, where you have breakfast and dinner.</p>
    <a>Read More</a>
  </div>
</section>

<section class="what">
  <h2 class="abs section-title" style="top:66px">What we do</h2>
  <p class="abs lead">Lorem ipsum dolor sit amet, consectetur adipiscing elit, sed do eiusmod tempor incididunt ut labore et dolore magna aliqua. Ut enim ad minim veniam, quis nostrud exercitation ullamco laboris nisi ut aliquip ex ea commodo consequat.</p>
  <svg class="abs" style="left:0;top:0" width="1200" height="824">
    <path d="M469 278 A163 163 0 1 0 729 278" fill="none" stroke="var(--blue)" stroke-width="3.5"/>
    <g fill="#fff" stroke="var(--blue)" stroke-width="2.5">
      <circle cx="469" cy="278" r="7"/><circle cx="729" cy="278" r="7"/>
      <circle cx="446" cy="445" r="7"/><circle cx="748" cy="445" r="7"/>
      <circle cx="598" cy="542" r="7"/>
    </g>
  </svg>
  <div class="abs hub-name">lernwandel</div>

  <span class="abs step-icon" style="left:332px;top:242px;background:var(--blue)"><svg width="50" height="50"><use href="#coin-hand"/></svg></span>
  <span class="abs step-icon" style="left:329px;top:407px;background:var(--orange)"><svg width="50" height="50"><use href="#coin-hand"/></svg></span>
  <span class="abs step-icon" style="left:782px;top:242px;background:var(--orange)"><svg width="50" height="50"><use href="#coin-hand"/></svg></span>
  <span class="abs step-icon" style="left:782px;top:407px;background:var(--orange)"><svg width="50" height="50"><use href="#coin-hand"/></svg></span>
  <span class="abs step-icon" style="left:554px;top:575px;background:var(--orange)"><svg width="50" height="50"><use href="#coin-hand"/></svg></span>

  <p class="abs step-text left" style="right:882px;top:254px">Lorem ipsum dolor sit amet,<br>labore et dolore magna aliqua.</p>
  <p class="abs step-text left" style="right:882px;top:420px">Lorem ipsum dolor sit amet,<br>labore et dolore magna aliqua.</p>
  <p class="abs step-text" style="left:881px;top:254px">Lorem ipsum dolor sit amet,<br>labore et dolore magna aliqua.</p>
  <p class="abs step-text" style="left:881px;top:420px">Lorem ipsum dolor sit amet,<br>labore et dolore magna aliqua.</p>
  <p class="abs step-text" style="left:0;right:0;text-align:center;top:682px">Lorem ipsum dolor sit amet,<br>labore et dolore magna aliqua.</p>
</section>

<section class="contact">
  <h2 class="abs section-title">Contact Us</h2>
  <div class="abs field" style="left:180px;top:153px;width:414px;height:51px">Name</div>
  <div class="abs field" style="left:604px;top:153px;width:414px;height:51px">Email</div>
  <div class="abs field" style="left:180px;top:215px;width:414px;height:51px">Phone Number</div>
  <div class="abs field" style="left:604px;top:215px;width:414px;height:51px">Subject</div>
  <div class="abs field" style="left:180px;top:278px;width:838px;height:87px">Message</div>
  <a class="abs btn">Submit</a>
</section>

<section class="partners">
  <h2 class="abs section-title" style="top:72px">Our Partners</h2>
  <svg class="abs" style="left:56px;top:222px" width="16" height="24"><path d="M12 3L4 12l8 9" fill="none" stroke="#555" stroke-width="2"/></svg>
  <svg class="abs" style="left:1140px;top:222px" width="16" height="24"><path d="M4 3l8 9-8 9" fill="none" stroke="#222" stroke-width="2.5"/></svg>
  <div class="abs partner" style="left:101px"><span role="img" aria-label="Partner badge"></span></div>
  <div class="abs partner" style="left:306px"><span role="img" aria-label="Partner badge"></span></div>
  <div class="abs partner" style="left:511px"><span role="img" aria-label="Partner badge"></span></div>
  <div class="abs partner" style="left:716px"><span role="img" aria-label="Partner badge"></span></div>
  <div class="abs partner" style="left:921px"><span role="img" aria-label="Partner badge"></span></div>
</section>

<footer class="site-footer">
  <div class="abs footer-brand">lernwandel</div>
  <span class="abs f-social" style="left:99px" aria-label="Social network link"></span>
  <span class="abs f-social" style="left:141px" aria-label="Social network link"></span>
  <span class="abs f-social" style="left:184px" aria-label="Social network link"></span>
  <div class="abs iban-label">IBAN Number :</div>
  <div class="abs iban">CH00 0000 0000 0001</div>

  <div class="abs f-col" style="left:367px;top:68px">
    <h4>Quick Links</h4>
    <ul>
      <li>➜ What we do</li><li>➜ Registration</li><li>➜ Company</li><li>➜ Host Family</li><li>➜ About Us</li><li>➜ Contact</li>
    </ul>
  </div>
  <div class="abs f-col" style="left:599px;top:68px">
    <h4>Other Links</h4>
    <ul>
      <li>➜ FAQ</li><li>➜ Tems of Use</li><li>➜ Privacy Policy</li><li>➜ Support Links</li><li>➜ Conditions</li>
    </ul>
  </div>
  <div class="abs f-col f-contact" style="left:820px;top:68px">
    <h4>Contact Us</h4>
    <ul>
      <li><span class="f-pin"><svg width="12" height="16" viewBox="0 0 12 16"><path fill="#234f86" d="M6 0a6 6 0 0 0-6 6c0 4.5 6 10 6 10s6-5.5 6-10a6 6 0 0 0-6-6zm0 8.5A2.5 2.5 0 1 1 6 3.5a2.5 2.5 0 0 1 0 5z"/></svg></span>lernwandel Lindenweg 4, 3000 Bern</li>
      <li><span class="f-pin"><svg width="14" height="11" viewBox="0 0 24 18"><path fill="#234f86" d="M0 2l12 8 12-8V0H0zM0 4.5V18h24V4.5l-12 8z"/></svg></span>info@lernwandel.ch</li>
      <li><span class="f-pin"><svg width="14" height="14" viewBox="0 0 24 24"><path fill="#234f86" d="M6.6 10.8a15 15 0 0 0 6.6 6.6l2.2-2.2a1 1 0 0 1 1-.25 11 11 0 0 0 3.6.6 1 1 0 0 1 1 1V20a1 1 0 0 1-1 1A17 17 0 0 1 3 4a1 1 0 0 1 1-1h3.5a1 1 0 0 1 1 1 11 11 0 0 0 .6 3.6 1 1 0 0 1-.25 1z"/></svg></span>+41 (0) 31 555 01 23</li>
    </ul>
  </div>
  <div class="abs rule"></div>
  <div class="abs copyright">Copyrights@2023.lernwandel.All Rights Reserved</div>
  <div class="abs sponsor">Corvina Circle<i></i></div>
</footer>
</body>
</html>
```